Plakat Ausbildung für Handwerksbetrieb
Zielgruppe
Wir sind ein Handwerksbetrieb und möchten mit einem Banner auf unsere Ausbildungsplätze hinweisen und junge Menschen (vor allem Schüler + Studenten) ansprechen. Der Banner soll nach Möglichkeit quadratisch sein. Unser bisheriges Logo habe ich als Datei angehängt. Desweiteren ein Bild wie ich es mir in etwa vorstellen würde das sich die 3 Elemente (Feuer, Wasser und Strom als Synonym für Heizung, Sanitär und Elektro) darstellen. Dazu noch eine knappe Beschreibung welche Ausbildungsplätze wir anbieten und auf unsere Homepage verweisen.
Aufgabenstellung
Ausbildungsplätze als:
- Anlagenmechaniker/in für Sanitär-, Heizungs- und Klimatechnik
- Elektroinstallateur/in (Energie- und Gebäudetechnik)

```html
<!DOCTYPE html>
<html lang="de">
<head>
<meta charset="utf-8">
<title>HALVERS – Ausbildungsplätze</title>
<link href="https://fonts.googleapis.com/css2?family=Montserrat:wght@700;800&display=swap" rel="stylesheet">
<style>
  :root {
    --stage: #b3b3b3;
    --navy-deep: #04121f;
    --navy: #0b2a4a;
    --navy-glow: #134a7a;
    --yellow: #fdd20a;
    --white: #ffffff;
    --red: #e3202a;
    --fire: #f07a1a;
    --fire-dark: #5a1608;
    --water: #5fa8d8;
  }
  * { box-sizing: border-box; margin: 0; padding: 0; }
  html, body {
    width: 1200px; height: 1117px; overflow: hidden;
    background: var(--stage);
    font-family: "Montserrat", sans-serif;
  }
  .banner {
    position: absolute; left: 135px; top: 94px;
    width: 929px; height: 929px; overflow: hidden;
    background: radial-gradient(circle at 30% 45%, var(--navy-glow) 0%, var(--navy) 35%, var(--navy-deep) 85%);
  }
  .hero-visual {
    position: absolute; left: 380px; top: 0; width: 549px; height: 929px;
    background:
      radial-gradient(ellipse at 62% 52%, #ffb028 0%, var(--fire) 25%, rgba(200,60,15,0.85) 45%, rgba(90,22,8,0) 70%),
      linear-gradient(90deg, rgba(11,42,74,0) 0%, rgba(95,168,216,0.35) 30%, rgba(180,70,20,0.7) 60%, var(--fire-dark) 100%);
  }
  .brand {
    position: absolute; left: 80px; top: 73px;
    display: flex; align-items: flex-start; gap: 14px;
  }
  .brand-mark {
    width: 87px; height: 87px; background: var(--white); border-radius: 4px; flex: none;
  }
  .brand-text {
    display: flex; flex-direction: column; padding-top: 1px;
  }
  .brand-name {
    font-weight: 800; font-size: 54px; line-height: 54px; color: var(--white);
    letter-spacing: 0.5px; white-space: nowrap;
  }
  .brand-tagline {
    margin-top: 4px; padding: 3px 0 4px;
    border-top: 3px solid var(--white); border-bottom: 3px solid var(--white);
    font-weight: 700; font-size: 14px; line-height: 17px; color: var(--yellow);
    text-align: center; white-space: nowrap;
  }
  .headline {
    position: absolute; left: 74px; top: 222px;
    font-weight: 800; font-size: 50px; line-height: 54px; color: var(--white);
    text-shadow: 0 3px 10px rgba(0,0,0,0.5);
  }
  .headline .accent { color: var(--yellow); }
  .job {
    position: absolute; left: 55px; width: 300px; text-align: center;
    color: var(--white); font-weight: 700; font-size: 20px; line-height: 29px;
  }
  .job-icon {
    display: block; margin: 0 auto 16px; width: 92px; height: 92px;
  }
  .job.mechanic { top: 431px; }
  .job.electric { top: 668px; }
  .job-title { display: block; white-space: nowrap; }
  .web-tab { position: absolute; left: 0; top: 0; width: 929px; height: 929px; }
  .web-url {
    position: absolute; left: 470px; width: 356px; top: 866px; text-align: center;
    color: var(--white); font-weight: 700; font-size: 20px; white-space: nowrap;
  }
</style>
</head>
<body>
<main class="banner">
  <div class="hero-visual" role="img" aria-label="Eishockeypuck zwischen spritzendem Wasser, Flammen und Blitzen als Sinnbild für Sanitär, Heizung und Elektro"></div>

  <header class="brand">
    <div class="brand-mark"></div>
    <div class="brand-text">
      <div class="brand-name">HALVERS</div>
      <div class="brand-tagline">HEIZUNG · SANITÄR · ELEKTRO</div>
    </div>
  </header>

  <h1 class="headline">
    WIR BIETEN EINEN<br>
    <span class="accent">AUSBILDUNG-<br>SPLÄTZE ALS</span>
  </h1>

  <section class="job mechanic">
    <svg class="job-icon" viewBox="0 0 92 92" aria-hidden="true">
      <circle cx="46" cy="46" r="42" fill="var(--navy-deep)" stroke="var(--white)" stroke-width="5"/>
      <g fill="none" stroke="var(--yellow)" stroke-width="3" stroke-linejoin="round">
        <path d="M46 46 C40 34 40 22 50 20 C60 19 60 32 46 46Z"/>
        <path d="M46 46 C58 40 70 42 70 52 C69 62 56 60 46 46Z"/>
        <path d="M46 46 C50 58 46 70 36 68 C27 65 32 54 46 46Z"/>
        <path d="M46 46 C34 50 22 48 22 38 C24 29 36 32 46 46Z"/>
        <circle cx="46" cy="46" r="4"/>
      </g>
    </svg>
    <span class="job-title">Anlagenmechaniker/in<br>für Sanitär-, Heizungs-<br>und Klimatechnik</span>
  </section>

  <section class="job electric">
    <svg class="job-icon" viewBox="0 0 92 92" aria-hidden="true">
      <circle cx="46" cy="46" r="42" fill="var(--navy-deep)" stroke="var(--white)" stroke-width="5"/>
      <g fill="none" stroke="var(--yellow)" stroke-width="3" stroke-linejoin="round">
        <path d="M41 14h10l2 8 6 3 7-5 7 7-5 7 3 6 8 2v10l-8 2-3 6 5 7-7 7-7-5-6 3-2 8H41l-2-8-6-3-7 5-7-7 5-7-3-6-8-2V41l8-2 3-6-5-7 7-7 7 5 6-3z"/>
        <circle cx="46" cy="46" r="15"/>
        <path d="M49 36 L41 48 H47 L43 57 L52 44 H46 Z"/>
      </g>
    </svg>
    <span class="job-title">Elektroinstallateur/in<br>(Energie- und<br>Gebäudetechnik)</span>
  </section>

  <svg class="web-tab" viewBox="0 0 929 929" aria-hidden="true">
    <path d="M420 929 L480 852 Q490 840 506 840 L782 840 Q800 840 812 855 L840 890 Q855 905 880 905 L929 905 L929 929 Z" fill="var(--red)"/>
  </svg>
  <div class="web-url">haustechnik-halvers-nord.de</div>
</main>
</body>
</html>
```